Website re-design

We are a successful furnished apartment provider in Boston. We currently are working on re-designing our website www.ribtenlofts.com to make it more modern, designer look and user friendly. We hired a designer, but are not happy with the designs proposed and want to improve on them. The winning design will be paid regardless of whether we stay with our current designer or not. We want ideas and functional page links to see how it will work. Platform we have chosen is wordpress. Feel free to propose others easy for us to update and modify. We do not like Joomla on which website is currently running. We do not like flash nor long load times.
Please use photos on our website for design presentations. www.ribtenlofts.com

Target Market(s)

doctors, nurses, business men but mostly business women, some post-medical students

Industry/Entity Type

Apartment

Requirements
Must have
• Quick action button for reservation form and a notification and email forwarding system to us of reservation information by potential clients. Blog required with feedback by guests allowed, we can censor which are published. Slide shows of apartments.
Should not have
• No movies.

```html
<!DOCTYPE html>
<html lang="en">
<head>
<meta charset="utf-8">
<title>Ribten Lofts Furnished Apartments</title>
<link rel="stylesheet" href="https://fonts.googleapis.com/css2?family=Open+Sans:wght@400;600;700&family=PT+Sans:wght@400;700&display=swap">
<style>
:root{
  --page:#f3f3f3;
  --ink:#222;
  --brand:#3a3020;
  --gold:#c9a24a;
  --orange:#f05a14;
  --purple:#4a2a8a;
  --navy:#14218a;
  --band:#1c4c7c;
  --band-dark:#143a62;
  --nav:#2c2c2c;
  --rose:#d4c0bf;
  --rose-line:#8a6c66;
  --field:#f5e1cf;
  --news-title:#6b4a44;
  --date:#1f5fd8;
  --footer:#3a3838;
  --footer-line:#6a6666;
  --footer-head:#f0972e;
  --green:#6fbf2c;
  --green-dark:#4e9a1e;
}
*{box-sizing:border-box;margin:0;padding:0}
html,body{width:1167px;height:1200px;overflow:hidden}
body{background:var(--page);font-family:"Open Sans",Arial,sans-serif;color:var(--ink);position:relative}
h1,h2,h3{font-weight:400}
.abs{position:absolute}

/* header */
.logo-mark{left:59px;top:38px;width:68px;height:68px;border-radius:50%;background:var(--gold)}
.brand-name{left:148px;top:52px;font-size:38px;color:var(--brand);line-height:1;letter-spacing:1px}
.brand-tag{left:152px;top:102px;font-size:11.5px;letter-spacing:3.3px;color:var(--brand);font-weight:600}
.phone{right:104px;top:24px;text-align:right;line-height:1}
.phone-number{font-size:20px;font-weight:700;color:var(--orange)}
.phone-hours{font-size:14px;color:var(--purple);margin-top:3px}
.agent-photo{left:1066px;top:9px;width:36px;height:57px;border-radius:4px;background:linear-gradient(#e8d8c8,#c8ccd6)}
.main-nav{left:487px;top:72px;width:622px;height:41px;display:flex;background:linear-gradient(#4a4a4a,var(--nav));border-radius:4px;box-shadow:0 6px 10px rgba(0,0,0,.18);overflow:hidden}
.main-nav a{display:flex;align-items:center;justify-content:center;color:#fff;text-decoration:none;font-size:15px;border-right:1px solid #1a1a1a}
.main-nav a.active{background:linear-gradient(#f6f6f6,#dcdcdc);color:#333;font-size:14px}

/* slideshow band */
.slide-band{left:0;top:146px;width:1167px;height:353px;background:radial-gradient(ellipse at center,var(--band),var(--band-dark))}
.slide-photo{left:181px;top:166px;width:833px;height:314px;border:4px solid #2a2a2a;background:linear-gradient(100deg,#8a7a52 0%,#d9c27a 35%,#e6d591 60%,#b59d63 100%)}
.slide-arrow{top:284px;font-size:60px;color:#c9d2dc;font-weight:300;line-height:1}

/* intro */
.welcome{left:64px;top:511px;font-size:19px;font-weight:700;color:var(--navy);letter-spacing:.6px}
.reserve-btn{left:848px;top:500px;width:280px;height:46px;border-radius:6px;background:linear-gradient(var(--green),var(--green-dark));transform:rotate(3deg);display:flex;align-items:center;justify-content:center;font-size:22px;font-weight:700;color:#fff;text-decoration:none;box-shadow:0 2px 4px rgba(0,0,0,.2)}
.intro{left:64px;top:559px;width:1040px;font-size:13.3px;line-height:22.8px;letter-spacing:.2px}

/* panels */
.panel{top:690px;height:256px;border-radius:5px}
.availability{left:40px;width:349px;background:var(--rose)}
.panel-title-rose{left:33px;top:14px;width:301px;font-family:"PT Sans",sans-serif;font-size:20px;color:#4a3a30;border-bottom:1px solid var(--rose-line);padding:0 0 2px 0}
.field-label{left:40px;font-size:14px;color:#8a5a20;font-weight:600}
.select{height:28px;border-radius:6px;background:var(--field);font-size:13.5px;color:#444;padding:5px 12px;display:flex;justify-content:space-between;align-items:center;box-shadow:inset 0 1px 2px rgba(0,0,0,.08)}
.select::after{content:"";border:5px solid transparent;border-top:6px solid #c8382a;margin-top:5px}
.check-btn{left:168px;top:207px;width:156px;height:38px;border-radius:7px;background:linear-gradient(#fff,#e6e6e6);box-shadow:0 1px 3px rgba(0,0,0,.3);display:flex;align-items:center;justify-content:center;font-family:"PT Sans",sans-serif;font-size:15.5px;color:#333}
.news{left:399px;width:370px;background:#fff;border:1px solid #d4d4d4;box-shadow:0 1px 4px rgba(0,0,0,.12)}
.news-title{left:21px;top:8px;font-family:"PT Sans",sans-serif;font-size:25px;color:var(--news-title)}
.news-date{right:28px;font-size:12.5px;color:var(--date)}
.news-text{font-size:12.3px;line-height:16px;width:260px}
.gallery{left:781px;width:342px;background:#fff;border:1px solid #d4d4d4;box-shadow:0 1px 4px rgba(0,0,0,.12);overflow:hidden}
.gallery-head{left:0;top:0;width:100%;height:50px;background:linear-gradient(#fff,#e9e9e9);border-bottom:1px solid #d0d0d0;font-family:"PT Sans",sans-serif;font-size:25px;color:#333;padding:6px 26px}
.thumb{width:100px;height:64px;background:linear-gradient(120deg,#7a5a3a,#d8b890 55%,#a07048)}

/* footer */
.site-footer{left:0;top:954px;width:1167px;height:246px;background:var(--footer)}
.foot-head{font-size:21px;color:var(--footer-head);line-height:1}
.foot-rule{height:1px;background:#9a9a9a}
.foot-divider{top:34px;width:1px;height:184px;background:var(--footer-line)}
.email-label{left:82px;top:73px;font-size:13px;color:#cfcfcf}
.email-input{left:82px;top:97px;width:271px;height:28px;background:#fff;border:1px solid #999}
.subscribe-btn{left:81px;top:136px;width:106px;height:23px;border-radius:12px;background:linear-gradient(#fafafa,#cfcfcf);font-size:13px;color:#444;display:flex;align-items:center;justify-content:center;letter-spacing:.5px}
.social{top:79px;width:34px;height:34px;border-radius:4px}
.foot-links{left:732px;top:30px;list-style:none}
.foot-links li{font-size:13px;color:#ddd;height:25px;display:flex;align-items:center;gap:12px}
.foot-links li::before{content:"";width:6px;height:6px;border-right:2px solid #fff;border-top:2px solid #fff;transform:rotate(45deg)}
.map{left:919px;top:64px;width:209px;height:157px;background:linear-gradient(135deg,#e6e2d6,#d4d0c4 50%,#c9d3dc);border:2px solid #fff}
</style>
</head>
<body>

<header>
  <div class="abs logo-mark"></div>
  <div class="abs brand-name">RIBTEN LOFTS</div>
  <div class="abs brand-tag">FURNISHED APARTMENTS</div>
  <div class="abs phone">
    <div class="phone-number">617 555 0192</div>
    <div class="phone-hours">24 x 7</div>
  </div>
  <div class="abs agent-photo" role="img" aria-label="Photo of a support agent with headset"></div>
  <nav class="abs main-nav">
    <a href="#" style="width:94px" aria-label="Home">
      <svg width="20" height="18" viewBox="0 0 20 18"><path d="M10 1 1 9h3v8h4v-5h4v5h4V9h3z" fill="#fff"/></svg>
    </a>
    <a href="#" class="active" style="width:111px">Links</a>
    <a href="#" style="width:115px">Rates</a>
    <a href="#" style="width:112px">Reviews</a>
    <a href="#" style="width:190px;border-right:0">Apartments</a>
  </nav>
</header>

<section>
  <div class="abs slide-band"></div>
  <div class="abs slide-photo" role="img" aria-label="Slideshow photo of a furnished studio apartment with armchairs and bed"></div>
  <div class="abs slide-arrow" style="left:76px">&lt;</div>
  <div class="abs slide-arrow" style="left:1055px">&gt;</div>
</section>

<section>
  <h1 class="abs welcome">Welcome to Ribten Lofts Furnished Apartments</h1>
  <a href="#" class="abs reserve-btn">Reserve Now</a>
  <p class="abs intro">Ribten Lofts is proud to offer some of the best furnished apartments in Boston. Our locations are in the trendiest area of the city: the South End. In the South End neighborhood, you will find wonderful restaurants, theaters, cafes and artist lofts. Our short term and extended stay apartments are very, very clean. We also offer the latest designer layouts: hardwood floors, Wireless Dsl, Cable TV, flat screen in most apartments, washer and dryer, cookware, cotton linens. Please click links on left for photo galleries, pricing, availability and reservation form and write us for more information. Thank you.</p>
</section>

<section class="abs panel availability">
  <h2 class="abs panel-title-rose">Check Availability</h2>
  <div class="abs field-label" style="top:67px">Chick IN Date :</div>
  <div class="abs select" style="left:45px;top:91px;width:110px">Tue 21</div>
  <div class="abs select" style="left:193px;top:91px;width:131px">December</div>
  <div class="abs field-label" style="top:134px">Chick Out Date :</div>
  <div class="abs select" style="left:45px;top:160px;width:110px">Tue 21</div>
  <div class="abs select" style="left:193px;top:160px;width:131px">December</div>
  <div class="abs check-btn">Check Availability</div>
</section>

<section class="abs panel news">
  <h2 class="abs news-title">Latest News</h2>
  <div class="abs news-date" style="top:54px">Monday, 20th&nbsp; JAN</div>
  <p class="abs news-text" style="left:48px;top:76px">Aenean felis mi, suscipit ut aliquam at, eleifend accumsan sem.</p>
  <div class="abs news-date" style="top:125px">Monday, 20th&nbsp; JAN</div>
  <p class="abs news-text" style="left:51px;top:150px">Aenean felis mi, suscipit ut aliquam at, eleifend accumsan sem.</p>
  <div class="abs news-date" style="top:189px">Monday, 20th&nbsp; JAN</div>
  <p class="abs news-text" style="left:55px;top:213px">Aenean felis mi, suscipit ut aliquam at, eleifend accumsan sem.</p>
</section>

<section class="abs panel gallery">
  <h2 class="abs gallery-head">Photo Gallery</h2>
  <div class="abs thumb" style="left:15px;top:73px" role="img" aria-label="Apartment photo thumbnail"></div>
  <div class="abs thumb" style="left:119px;top:73px" role="img" aria-label="Apartment photo thumbnail"></div>
  <div class="abs thumb" style="left:229px;top:73px" role="img" aria-label="Apartment photo thumbnail"></div>
  <div class="abs thumb" style="left:15px;top:160px" role="img" aria-label="Apartment photo thumbnail"></div>
  <div class="abs thumb" style="left:119px;top:160px" role="img" aria-label="Apartment photo thumbnail"></div>
  <div class="abs thumb" style="left:229px;top:160px" role="img" aria-label="Apartment photo thumbnail"></div>
</section>

<footer class="abs site-footer">
  <h3 class="abs foot-head" style="left:82px;top:37px">Subscribe by Email</h3>
  <div class="abs foot-rule" style="left:82px;top:64px;width:339px"></div>
  <div class="abs email-label">Email Address</div>
  <div class="abs email-input"></div>
  <div class="abs subscribe-btn">Subscribe</div>

  <div class="abs foot-divider" style="left:442px"></div>
  <h3 class="abs foot-head" style="left:463px;top:38px">Follow us on</h3>
  <div class="abs foot-rule" style="left:463px;top:65px;width:213px"></div>
  <div class="abs social" style="left:465px;background:#6cc3e6" aria-label="Social link"></div>
  <div class="abs social" style="left:533px;background:#3b5b9a" aria-label="Social link"></div>
  <div class="abs social" style="left:601px;background:#2a7fb8" aria-label="Social link"></div>

  <div class="abs foot-divider" style="left:687px"></div>
  <ul class="abs foot-links">
    <li>Contact</li><li>Apartments</li><li>Reservations</li><li>Links</li><li>Locations</li><li>Rates</li><li>Blog</li>
  </ul>

  <div class="abs foot-divider" style="left:897px"></div>
  <h3 class="abs foot-head" style="left:1049px;top:32px;font-size:19px">FIND US</h3>
  <div class="abs map" role="img" aria-label="Street map showing the apartment locations"></div>
</footer>

</body>
</html>
```